Dozing Heron

Need a business card for our restaurant. Restaurant and Bar in the mountains of North Idaho. Rustic looking card

Contact Information for Business Card

rustic design, wood and metal looking, primarily neutral colors

Requirements
Must have
• Name, address, phone number, website, email address

```html
<!DOCTYPE html>
<html lang="en">
<head>
<meta charset="utf-8">
<title>The Dozing Heron – Business Card</title>
<link href="https://fonts.googleapis.com/css2?family=Lato:wght@400&family=Marcellus&family=Permanent+Marker&display=swap" rel="stylesheet">
<style>
  :root {
    --stage: #2b2b2b;
    --card-base: #141414;
    --card-mid: #262626;
    --card-light: #333333;
    --ink: #f2f2f2;
    --ink-soft: #d9d9d9;
    --mark-area: #cfcfcf;
  }
  * { margin: 0; padding: 0; box-sizing: border-box; }
  html, body {
    width: 1200px;
    height: 875px;
    overflow: hidden;
    background: var(--stage);
  }
  .stage {
    position: relative;
    width: 1200px;
    height: 875px;
    display: flex;
    align-items: center;
    justify-content: center;
    gap: 40px;
  }
  .card {
    position: relative;
    width: 540px;
    height: 309px;
    border-radius: 18px;
    overflow: hidden;
    background:
      radial-gradient(ellipse 60% 45% at 70% 30%, rgba(70,70,70,0.55), transparent 70%),
      radial-gradient(ellipse 50% 40% at 20% 75%, rgba(55,55,55,0.5), transparent 70%),
      radial-gradient(ellipse 35% 30% at 45% 55%, rgba(40,40,40,0.6), transparent 75%),
      linear-gradient(135deg, var(--card-mid), var(--card-base) 60%, #0d0d0d);
  }

  /* Front */
  .card-front {
    display: flex;
    align-items: center;
    justify-content: center;
    gap: 14px;
  }
  .brand-dot {
    width: 16px;
    height: 16px;
    border-radius: 50%;
    background: var(--ink);
  }
  .brand-name {
    font-family: "Marcellus", serif;
    font-size: 34px;
    letter-spacing: 3px;
    text-transform: uppercase;
    color: var(--ink);
  }

  /* Back */
  .brand-mark-area {
    position: absolute;
    right: 34px;
    top: 28px;
    width: 190px;
    height: 250px;
    display: flex;
    align-items: center;
    justify-content: center;
  }
  .brand-mark-area .brand-name {
    font-size: 30px;
    line-height: 1.15;
    text-align: center;
    color: var(--mark-area);
  }
  .contact {
    position: absolute;
    left: 34px;
    bottom: 30px;
    color: var(--ink);
  }
  .contact-name {
    font-family: "Permanent Marker", cursive;
    font-size: 26px;
    letter-spacing: 1.5px;
    line-height: 1.1;
  }
  .contact-role {
    font-family: "Lato", sans-serif;
    font-size: 15px;
    color: var(--ink-soft);
    margin-bottom: 12px;
  }
  .contact-list {
    list-style: none;
    font-family: "Lato", sans-serif;
    font-size: 13px;
    color: var(--ink-soft);
  }
  .contact-list li {
    display: flex;
    align-items: center;
    gap: 9px;
    line-height: 22px;
  }
  .contact-list svg {
    width: 11px;
    height: 11px;
    fill: none;
    stroke: var(--ink-soft);
    stroke-width: 1.6;
    flex: none;
  }
</style>
</head>
<body>
<main class="stage">

  <section class="card card-front" aria-label="Card front">
    <span class="brand-dot"></span>
    <span class="brand-name">The Dozing Heron</span>
  </section>

  <section class="card card-back" aria-label="Card back">
    <div class="brand-mark-area">
      <span class="brand-name">Dozing<br>Heron</span>
    </div>

    <div class="contact">
      <p class="contact-name">OWEN PARKER</p>
      <p class="contact-role">Founder &amp; CEO</p>
      <ul class="contact-list">
        <li>
          <svg viewBox="0 0 12 12"><path d="M2 1.5h2.5l1 2.5-1.5 1a6 6 0 0 0 3 3l1-1.5 2.5 1V10a1 1 0 0 1-1 1A9 9 0 0 1 1 2.5a1 1 0 0 1 1-1z"/></svg>
          (208) 555-0147
        </li>
        <li>
          <svg viewBox="0 0 12 12"><rect x="1" y="2.5" width="10" height="7" rx="0.5"/><path d="M1 3l5 3.5L11 3"/></svg>
          info@thedozingheronpinecrest.com
        </li>
        <li>
          <svg viewBox="0 0 12 12"><circle cx="6" cy="6" r="5"/><ellipse cx="6" cy="6" rx="2.2" ry="5"/><path d="M1 6h10"/></svg>
          thedozingheronpinecrest.com
        </li>
        <li>
          <svg viewBox="0 0 12 12"><path d="M6 11s-3.5-3.6-3.5-6a3.5 3.5 0 0 1 7 0C9.5 7.4 6 11 6 11z"/><circle cx="6" cy="5" r="1.2"/></svg>
          214 Cedar St, Pinecrest, ID 83800
        </li>
      </ul>
    </div>
  </section>

</main>
</body>
</html>
```